Weight loss surgery restaurant card

We need to create a card for patients who have undergone weight loss surgery to take to restaurants so they can request smaller meals. These patients have had surgery on their stomach so that they can only consume half to one cup of food at a time. So normal sized restaurant meals are way too big (and cost a lot). This card they can present to the restaurant to communicate the fact that they have had weight loss surgery and therefore request a smaller meal portion at reduced cost

Target Market(s)

Restaurants serving weight loss surgery patients

Industry/Entity Type

Health Care

Contact Information for Business Card

This will be a plastic card similar to business card size.

Requirements
Must have
• The front of the card should include the following text:
• The individual bearing this card has undergone weight loss surgery.
• This surgery restricts portion sizes to between half and one cup of food at a time.
• Please give consideration to allowing smaller portions of your regular meals to be ordered to reduce wastage and excess costs.
• Example: a half size portion priced at two thirds of usual cost.
• The back of the card will have spaces for the person to write certain information. These are the categories that can be filled in by hand:
• Name:
• Procedure performed:
• Date of procedure (month/year):
• Treating Clinic Name:
• Treating Clinic Signature:
• Somewhere down the bottom should be something along the lines of:
• supplied from bernardwhitlow.com.au
Nice to have
• A nice design with imagery/colours etc ... not just the text on a white background! Bright attractive colours preferred.
• I have uploaded my logo ... a roughly triangular image followed by my name etc. The triangular logo image could be used somewhere on the card and this logo can be interchangeable for other clinics who purchase the card.
• **Please note that I don't want my name to be included as part of the logo on the card ... just use the triangular image on the side of the logo without the following name**
• Also, the colouring of the card does not have to reflect my logo colours as I am anticipating interchanging this logo with other logos if other clinics choose to adopt the card. I am interested to see other, more generic, colour choices as well as my logo colours

```html
<!DOCTYPE html>
<html lang="en">
<head>
<meta charset="utf-8">
<title>Bariatric Portion Card</title>
<link rel="stylesheet" href="https://fonts.googleapis.com/css2?family=Noto+Serif:wght@400&display=swap">
<style>
  :root {
    --teal: #16968a;
    --teal-dark: #0f7f75;
    --paper: #ffffff;
    --ink: #1b1b1b;
    --muted: #7d8a89;
    --backdrop: #d9d9d9;
  }
  html, body {
    margin: 0;
    padding: 0;
    width: 1200px;
    height: 864px;
    overflow: hidden;
    background: var(--backdrop);
  }
  .canvas {
    position: relative;
    width: 1200px;
    height: 864px;
  }
  .card {
    position: absolute;
    width: 620px;
    height: 360px;
    background: var(--teal);
    border-radius: 6px;
    box-shadow: 0 6px 18px rgba(0,0,0,0.18);
    overflow: hidden;
    font-family: "Noto Serif", serif;
    color: var(--ink);
  }
  .card--notice { left: 520px; top: 50px; }
  .card--details { left: 60px; top: 450px; }
  .card__panel {
    position: absolute;
    inset: 0;
    background: var(--paper);
    border-radius: 120px 0 120px 0;
  }
  .brand {
    position: absolute;
    top: 40px;
    left: 0;
    right: 0;
    display: flex;
    justify-content: center;
    align-items: center;
    gap: 14px;
  }
  .brand__dot {
    width: 40px;
    height: 40px;
    border-radius: 50%;
    background: var(--teal);
  }
  .brand__text { line-height: 1; }
  .brand__name {
    font-size: 30px;
    color: var(--teal);
    letter-spacing: 1px;
  }
  .brand__role {
    font-size: 10px;
    color: var(--teal);
    letter-spacing: 2.5px;
    text-transform: uppercase;
    margin-top: 5px;
  }
  .notice-list {
    position: absolute;
    top: 128px;
    left: 62px;
    right: 40px;
    margin: 0;
    padding: 0;
    list-style: none;
    font-size: 15.5px;
    line-height: 1.22;
  }
  .notice-list li {
    position: relative;
    padding-left: 24px;
    margin-bottom: 4px;
  }
  .notice-list li::before {
    content: "";
    position: absolute;
    left: 2px;
    top: 5px;
    width: 11px;
    height: 11px;
    border-radius: 50%;
    background: var(--teal);
  }
  .form {
    position: absolute;
    top: 118px;
    left: 52px;
    right: 44px;
    font-size: 17px;
  }
  .form__row {
    display: flex;
    align-items: baseline;
    gap: 8px;
    height: 32px;
  }
  .form__label { white-space: nowrap; }
  .form__line {
    flex: 1;
    border-bottom: 1.5px dashed var(--ink);
    transform: translateY(-4px);
  }
  .supplied {
    position: absolute;
    left: 52px;
    bottom: 38px;
    font-size: 24px;
    color: var(--teal);
  }
</style>
</head>
<body>
<main class="canvas">

  <section class="card card--notice" aria-label="Card front">
    <div class="card__panel"></div>
    <header class="brand">
      <span class="brand__dot"></span>
      <div class="brand__text">
        <div class="brand__name">Bernard Whitlow</div>
        <div class="brand__role">General, Upper GI &amp; Bariatric Surgeon</div>
      </div>
    </header>
    <ul class="notice-list">
      <li>The individual bearing this card has undergone weight loss surgery</li>
      <li>This surgery restricts portion sizes to between half and one cup of food at a time</li>
      <li>Please give consideration to allowing smaller portions of your regular meals to be ordered to reduce wastage and excess costs.</li>
      <li>Example: a half size portion priced at two thirds of usual cost.</li>
    </ul>
  </section>

  <section class="card card--details" aria-label="Card back">
    <div class="card__panel"></div>
    <header class="brand">
      <span class="brand__dot"></span>
      <div class="brand__text">
        <div class="brand__name">Bernard Whitlow</div>
        <div class="brand__role">General, Upper GI &amp; Bariatric Surgeon</div>
      </div>
    </header>
    <div class="form">
      <div class="form__row"><span class="form__label">Name :</span><span class="form__line"></span></div>
      <div class="form__row"><span class="form__label">Procedure performed :</span><span class="form__line"></span></div>
      <div class="form__row"><span class="form__label">Date of procedure (month/year) :</span><span class="form__line"></span></div>
      <div class="form__row"><span class="form__label">Treating Clinic Name :</span><span class="form__line"></span></div>
      <div class="form__row"><span class="form__label">Treating Clinic Signature :</span><span class="form__line"></span></div>
    </div>
    <p class="supplied">supplied from bernardwhitlow.com.au</p>
  </section>

</main>
</body>
</html>
```